Introductory Flyer

We need a flyer to make businesses aware of our services. We do 3D Printing with a K480 Kelmix Printer(ie make solid prototypes from drawings.

We are a newish company looking to get new business. Photos and text can be taken from our website www.brevalunsolutions.com.au and I have permision to use photos from www.kelmix.com if you need any extras. I could also write new text to suit your ideas.

3D Printing is a new technology.  People need to think "Hey! Look what this company can do for us."

Target Market(s)

Anyone designing or needing models of any solid object. Includes engineers, architects, councils, manufacturers. Need to send to businesses and get passed around rather than thrown out.

Industry/Entity Type

Manufacturing

Requirements
Must have
• Something quirky though not too expensive to print. Maybe folded popup card.

• Explain clearly what we actually do. ie 3D Printing and CAD Drawing.

• Not look out of accord with our website www.brevalunsolutions.com.au

Nice to have
• Prefer smaller card to A4 sheet. Something to fit in DL envelope. Needs to convey quality and high tech side of our business.

```html
<!DOCTYPE html>
<html lang="en">
<head>
<meta charset="utf-8">
<title>Brevalun Solutions – Ruler Flyer</title>
<link rel="stylesheet" href="https://fonts.googleapis.com/css2?family=Urbanist:wght@400;700&family=Arimo:wght@400;700&display=swap">
<style>
  :root {
    --stage: #000000;
    --card: #ffffff;
    --orange: #f6a04b;
    --ink: #3a2a1c;
    --white: #ffffff;
    --tick: #8a8a8a;
    --label: #ffffff;
  }
  * { box-sizing: border-box; margin: 0; padding: 0; }
  html, body { width: 1200px; height: 2523px; overflow: hidden; background: var(--stage); }
  body { position: relative; font-family: "Arimo", Arial, sans-serif; }

  .side-label {
    position: absolute; left: 16px;
    color: var(--label); font: 700 26px "Arimo", Arial, sans-serif;
  }
  .side-label--front { top: 585px; }
  .side-label--back  { top: 1255px; }

  .ruler-card {
    position: absolute; left: 0; width: 1200px; height: 550px;
    background: var(--card); overflow: hidden;
  }
  .ruler-card--front { top: 630px; }
  .ruler-card--back  { top: 1300px; }

  .scale { position: absolute; left: 0; width: 1200px; height: 110px; }
  .scale--top { top: 0; }
  .scale--bottom { top: 440px; }
  .scale text { font: 400 20px "Arimo", Arial, sans-serif; fill: var(--tick); text-anchor: middle; }

  .panel {
    position: absolute; top: 116px; height: 322px;
    background: var(--orange); color: var(--ink);
  }
  .ruler-card--front .panel { left: 303px; width: 878px; }
  .ruler-card--back .panel  { left: 15px;  width: 876px; }

  .slogan {
    position: absolute; color: var(--white);
    font: 400 36px/1.55 "Urbanist", "Century Gothic", sans-serif;
  }
  .slogan strong { font-weight: 700; font-size: 42px; }
  .ruler-card--front .slogan { left: 50px; top: 40px; }
  .ruler-card--back .slogan  { right: 50px; top: 38px; text-align: right; }

  .service-copy { position: absolute; font-size: 19px; line-height: 1.3; }
  .service-copy h2 { font: 400 24px "Arimo", Arial, sans-serif; margin-bottom: 10px; }
  .service-copy p { margin-bottom: 10px; }
  .service-copy .web { font-size: 21px; margin-top: 14px; }
  .ruler-card--front .service-copy { left: 405px; top: 34px; width: 450px; }
  .ruler-card--back .service-copy  { left: 40px; top: 34px; width: 430px; text-align: right; }
  .ruler-card--back .service-copy h2 { text-align: center; }
  .ruler-card--back .service-copy .web { text-align: left; }

  .brand {
    position: absolute; display: flex; align-items: center; gap: 10px;
    color: var(--orange); font: 700 26px/1.1 "Urbanist", "Century Gothic", sans-serif;
  }
  .brand__square { width: 26px; height: 26px; background: var(--orange); flex: none; }
  .ruler-card--front .brand { left: 40px; top: 240px; width: 250px; }
  .ruler-card--back .brand  { left: 912px; top: 240px; width: 270px; }
</style>
</head>
<body>
  <div class="side-label side-label--front">Front:</div>
  <section class="ruler-card ruler-card--front">
    <svg class="scale scale--top" viewBox="0 0 1200 110" aria-hidden="true">
      <defs>
        <pattern id="cm-top" x="38" y="0" width="55.7" height="110" patternUnits="userSpaceOnUse">
          <line x1="0.5" y1="0" x2="0.5" y2="40" stroke="#8a8a8a" stroke-width="1.4"/>
          <line x1="27.85" y1="0" x2="27.85" y2="28" stroke="#8a8a8a"/>
          <line x1="5.57" y1="0" x2="5.57" y2="16" stroke="#8a8a8a"/>
          <line x1="11.14" y1="0" x2="11.14" y2="16" stroke="#8a8a8a"/>
          <line x1="16.71" y1="0" x2="16.71" y2="16" stroke="#8a8a8a"/>
          <line x1="22.28" y1="0" x2="22.28" y2="16" stroke="#8a8a8a"/>
          <line x1="33.42" y1="0" x2="33.42" y2="16" stroke="#8a8a8a"/>
          <line x1="38.99" y1="0" x2="38.99" y2="16" stroke="#8a8a8a"/>
          <line x1="44.56" y1="0" x2="44.56" y2="16" stroke="#8a8a8a"/>
          <line x1="50.13" y1="0" x2="50.13" y2="16" stroke="#8a8a8a"/>
        </pattern>
      </defs>
      <rect x="38" y="0" width="1116" height="42" fill="url(#cm-top)"/>
      <text x="38" y="68">0</text><text x="149.4" y="68">2</text><text x="260.8" y="68">4</text>
      <text x="372.2" y="68">6</text><text x="483.6" y="68">8</text><text x="595" y="68">10</text>
      <text x="706.4" y="68">12</text><text x="817.8" y="68">14</text><text x="929.2" y="68">16</text>
      <text x="1040.6" y="68">18</text><text x="1152" y="68">20</text>
    </svg>

    <div class="brand"><span class="brand__square"></span><span>Brevalun Solutions</span></div>

    <div class="panel">
      <p class="slogan">“communicate<br>your <strong>ideas</strong><br><strong>in 3D</strong> quickly<br>and easily”</p>
      <div class="service-copy">
        <h2>Offering 3D modeling solutions</h2>
        <p>Using new 3D Printing technology we can jump start your design process by bringing amazing high definition 3D models into your hands quickly and affordably.</p>
        <p>Our 3D solutions are excellent for visual aids, prototypes, concept and evaluation models.</p>
        <p class="web">http://www.brevalunsolutions.com.au</p>
      </div>
    </div>

    <svg class="scale scale--bottom" viewBox="0 0 1200 110" aria-hidden="true">
      <defs>
        <pattern id="in-front" x="38" y="0" width="140" height="110" patternUnits="userSpaceOnUse">
          <line x1="0.5" y1="110" x2="0.5" y2="68" stroke="#8a8a8a" stroke-width="1.4"/>
          <line x1="70" y1="110" x2="70" y2="80" stroke="#8a8a8a"/>
          <line x1="35" y1="110" x2="35" y2="88" stroke="#8a8a8a"/>
          <line x1="105" y1="110" x2="105" y2="88" stroke="#8a8a8a"/>
          <line x1="17.5" y1="110" x2="17.5" y2="96" stroke="#8a8a8a"/>
          <line x1="52.5" y1="110" x2="52.5" y2="96" stroke="#8a8a8a"/>
          <line x1="87.5" y1="110" x2="87.5" y2="96" stroke="#8a8a8a"/>
          <line x1="122.5" y1="110" x2="122.5" y2="96" stroke="#8a8a8a"/>
        </pattern>
      </defs>
      <rect x="38" y="66" width="1122" height="44" fill="url(#in-front)"/>
      <text transform="translate(1158,42) rotate(180)">0</text>
      <text transform="translate(1018,42) rotate(180)">1</text>
      <text transform="translate(878,42) rotate(180)">2</text>
      <text transform="translate(738,42) rotate(180)">3</text>
      <text transform="translate(598,42) rotate(180)">4</text>
      <text transform="translate(458,42) rotate(180)">5</text>
      <text transform="translate(318,42) rotate(180)">6</text>
      <text transform="translate(178,42) rotate(180)">7</text>
      <text transform="translate(38,42) rotate(180)">8</text>
    </svg>
  </section>

  <div class="side-label side-label--back">Back:</div>
  <section class="ruler-card ruler-card--back">
    <svg class="scale scale--top" viewBox="0 0 1200 110" aria-hidden="true">
      <defs>
        <pattern id="cm-back" x="38" y="0" width="55.7" height="110" patternUnits="userSpaceOnUse">
          <line x1="0.5" y1="0" x2="0.5" y2="40" stroke="#8a8a8a" stroke-width="1.4"/>
          <line x1="27.85" y1="0" x2="27.85" y2="28" stroke="#8a8a8a"/>
          <line x1="5.57" y1="0" x2="5.57" y2="16" stroke="#8a8a8a"/>
          <line x1="11.14" y1="0" x2="11.14" y2="16" stroke="#8a8a8a"/>
          <line x1="16.71" y1="0" x2="16.71" y2="16" stroke="#8a8a8a"/>
          <line x1="22.28" y1="0" x2="22.28" y2="16" stroke="#8a8a8a"/>
          <line x1="33.42" y1="0" x2="33.42" y2="16" stroke="#8a8a8a"/>
          <line x1="38.99" y1="0" x2="38.99" y2="16" stroke="#8a8a8a"/>
          <line x1="44.56" y1="0" x2="44.56" y2="16" stroke="#8a8a8a"/>
          <line x1="50.13" y1="0" x2="50.13" y2="16" stroke="#8a8a8a"/>
        </pattern>
      </defs>
      <rect x="38" y="0" width="1116" height="42" fill="url(#cm-back)"/>
      <text transform="translate(38,68) scale(-1,1)">20</text>
      <text transform="translate(149.4,68) scale(-1,1)">18</text>
      <text transform="translate(260.8,68) scale(-1,1)">16</text>
      <text transform="translate(372.2,68) scale(-1,1)">14</text>
      <text transform="translate(483.6,68) scale(-1,1)">12</text>
      <text transform="translate(595,68) scale(-1,1)">10</text>
      <text transform="translate(706.4,68) scale(-1,1)">8</text>
      <text transform="translate(817.8,68) scale(-1,1)">6</text>
      <text transform="translate(929.2,68) scale(-1,1)">4</text>
      <text transform="translate(1040.6,68) scale(-1,1)">2</text>
      <text transform="translate(1152,68) scale(-1,1)">0</text>
    </svg>

    <div class="panel">
      <div class="service-copy">
        <h2>Specialising in rapid prototyping</h2>
        <p>Using up to date 3D printing technology we can make prototypes directly from CAD data.</p>
        <p>We offer a complete CAD Drawing service. From an email or telephone briefing we can provide CAD drawings and finally an actual model of your idea as quick as overnight.</p>
        <p class="web">http://www.brevalunsolutions.com.au</p>
      </div>
      <p class="slogan">“producing<br>quality <strong>3D</strong><br><strong>models</strong> from<br>your <strong>data</strong>”</p>
    </div>

    <div class="brand"><span class="brand__square"></span><span>Brevalun Solutions</span></div>

    <svg class="scale scale--bottom" viewBox="0 0 1200 110" aria-hidden="true">
      <defs>
        <pattern id="in-back" x="38" y="0" width="140" height="110" patternUnits="userSpaceOnUse">
          <line x1="0.5" y1="110" x2="0.5" y2="68" stroke="#8a8a8a" stroke-width="1.4"/>
          <line x1="70" y1="110" x2="70" y2="80" stroke="#8a8a8a"/>
          <line x1="35" y1="110" x2="35" y2="88" stroke="#8a8a8a"/>
          <line x1="105" y1="110" x2="105" y2="88" stroke="#8a8a8a"/>
          <line x1="17.5" y1="110" x2="17.5" y2="96" stroke="#8a8a8a"/>
          <line x1="52.5" y1="110" x2="52.5" y2="96" stroke="#8a8a8a"/>
          <line x1="87.5" y1="110" x2="87.5" y2="96" stroke="#8a8a8a"/>
          <line x1="122.5" y1="110" x2="122.5" y2="96" stroke="#8a8a8a"/>
        </pattern>
      </defs>
      <rect x="38" y="66" width="1122" height="44" fill="url(#in-back)"/>
      <text x="38" y="58">0</text><text x="178" y="58">1</text><text x="318" y="58">2</text>
      <text x="458" y="58">3</text><text x="598" y="58">4</text><text x="738" y="58">5</text>
      <text x="878" y="58">6</text><text x="1018" y="58">7</text><text x="1158" y="58">8</text>
    </svg>
  </section>
</body>
</html>
```